Design SOCIALPAGE and LinkedIn design for existing company

We have an existing website. We want a modern interactive SOCIALPAGE and LinkedIn design. Our website is www.CoverLantern.com

Target Market(s)

People aged 30-50. Family oriented

Industry/Entity Type

Life insurance

Font styles to use
Other font styles liked:
• Rubik

Colors
0054AA
0677BA
7BADD7
CADEEF
E8F1F8
00AB8E
00BBA5
67D7C9
C6EFE9
E9F9F6
59FF00
82FF00
B8FF75
E3FFCB
F4FFEA

Requirements
Must have
• It must be modern
Nice to have
• Same color scheme as website
Should not have
• Colors that deviate from our website

```html
<!DOCTYPE html>
<html lang="en">
<head>
<meta charset="utf-8">
<title>CoverLantern – Social Covers</title>
<link rel="stylesheet" href="https://fonts.googleapis.com/css2?family=Rubik:ital,wght@0,400;0,500;0,700;1,800&display=swap">
<style>
  :root{
    --page-bg:#F3FDD6;
    --brand-blue:#0054AA;
    --band-blue:#0B5BAE;
    --accent-green:#8CC63F;
    --soft-green:#A6D86A;
    --white:#FFFFFF;
    --sky:#F4E9E0;
    --sea:#7E9DB5;
    --surf:#D9E4EE;
  }
  *{margin:0;padding:0;box-sizing:border-box}
  html,body{width:1200px;height:1200px;overflow:hidden}
  body{background:var(--page-bg);font-family:"Rubik",sans-serif;position:relative}
  .platform-title{
    position:absolute;left:0;width:1200px;text-align:center;
    color:var(--brand-blue);font-weight:700;font-size:56px;letter-spacing:1px;line-height:1;
  }
  .platform-title--network{top:134px}
  .platform-title--social{top:622px}
  .cover{position:absolute;box-shadow:0 6px 12px rgba(0,0,0,.28);background:var(--white)}
  .cover svg{display:block;width:100%;height:100%}
  .cover--network{left:120px;top:228px;width:1003px;height:251px}
  .cover--social{left:125px;top:710px;width:998px;height:380px}
  .brand-name{font-family:"Rubik",sans-serif;font-weight:400;fill:var(--brand-blue)}
  .headline{font-family:"Rubik",sans-serif;font-weight:800;font-style:italic;fill:var(--white)}
  .feature-label{font-family:"Rubik",sans-serif;font-weight:500;fill:var(--white)}
  .feature-disc{fill:var(--white)}
  .feature-icon{fill:none;stroke:var(--accent-green);stroke-linecap:round;stroke-linejoin:round}
  .feature-icon-solid{fill:var(--accent-green)}
</style>
</head>
<body>

<h1 class="platform-title platform-title--network">Career NET</h1>

<div class="cover cover--network">
  <svg viewBox="0 0 1615 405" preserveAspectRatio="none">
    <defs>
      <linearGradient id="beachScene" x1="0" y1="0" x2="0" y2="1">
        <stop offset="0" stop-color="var(--sky)"/>
        <stop offset="0.1" stop-color="#C9D3DC"/>
        <stop offset="0.35" stop-color="var(--sea)"/>
        <stop offset="0.7" stop-color="var(--surf)"/>
        <stop offset="1" stop-color="#E7ECF1"/>
      </linearGradient>
    </defs>
    <g role="img" aria-label="Photo of a smiling family of four walking together along the beach by the surf">
      <rect x="0" y="0" width="1100" height="405" fill="url(#beachScene)"/>
    </g>
    <polygon points="0,0 222,0 0,212" fill="var(--accent-green)" opacity=".9"/>
    <polygon points="805,0 855,0 1020,405 970,405" fill="#C6D6E6" opacity=".7"/>
    <polygon points="800,405 1020,405 950,250" fill="var(--soft-green)" opacity=".9"/>
    <polygon points="855,0 1615,0 1615,405 1020,405" fill="var(--band-blue)"/>
    <polygon points="1218,0 1615,0 1615,92 1270,92" fill="var(--white)"/>
    <text class="brand-name" x="1572" y="62" font-size="42" text-anchor="end">CoverLantern</text>

    <text class="headline" x="1568" y="198" font-size="72" text-anchor="end">TERM LIFE</text>
    <text class="headline" x="1568" y="278" font-size="72" text-anchor="end">INSURANCE</text>

    <g class="feature feature--agent" transform="translate(1360,333)">
      <circle class="feature-disc" r="27"/>
      <circle class="feature-icon-solid" cx="0" cy="-4" r="7"/>
      <path class="feature-icon-solid" d="M-13 14 Q0 0 13 14 Z"/>
      <path class="feature-icon" stroke-width="2.5" d="M-10 -4 Q-10 -16 0 -16 Q10 -16 10 -4"/>
    </g>
    <g class="feature feature--compare" transform="translate(1452,333)">
      <circle class="feature-disc" r="27"/>
      <path class="feature-icon" stroke-width="3" d="M-8 -10 V8 M-8 -10 H6 M2 -14 L6 -10 L2 -6 M8 10 V-8 M8 10 H-6 M-2 14 L-6 10 L-2 6"/>
    </g>
    <g class="feature feature--apply" transform="translate(1547,333)">
      <circle class="feature-disc" r="27"/>
      <rect class="feature-icon-solid" x="-14" y="-13" width="24" height="12" rx="2"/>
      <path class="feature-icon-solid" d="M-6 -4 h6 v10 h8 v8 h-14 z"/>
    </g>
    <text class="feature-label" font-size="17" text-anchor="middle">
      <tspan x="1360" y="378">Agent</tspan><tspan x="1360" y="394">Support</tspan>
      <tspan x="1452" y="378">Compare</tspan><tspan x="1452" y="394">&amp; Save</tspan>
      <tspan x="1547" y="378">Apply</tspan><tspan x="1547" y="394">Online</tspan>
    </text>
  </svg>
</div>

<h1 class="platform-title platform-title--social">SOCIALPAGE</h1>

<div class="cover cover--social">
  <svg viewBox="0 0 1607 612" preserveAspectRatio="none">
    <defs>
      <linearGradient id="beachSceneTall" x1="0" y1="0" x2="0" y2="1">
        <stop offset="0" stop-color="var(--sky)"/>
        <stop offset="0.18" stop-color="#EADFD8"/>
        <stop offset="0.24" stop-color="#A9BCCB"/>
        <stop offset="0.45" stop-color="var(--sea)"/>
        <stop offset="0.75" stop-color="var(--surf)"/>
        <stop offset="1" stop-color="#E4E6E6"/>
      </linearGradient>
    </defs>
    <g role="img" aria-label="Photo of a smiling family of four walking together along the beach by the surf">
      <rect x="0" y="0" width="960" height="612" fill="url(#beachSceneTall)"/>
    </g>
    <polygon points="0,0 218,0 0,205" fill="var(--accent-green)" opacity=".9"/>
    <polygon points="620,0 672,0 912,612 860,612" fill="#C6D6E6" opacity=".7"/>
    <polygon points="672,612 912,612 820,440" fill="var(--soft-green)" opacity=".9"/>
    <polygon points="672,0 1607,0 1607,612 912,612" fill="var(--band-blue)"/>
    <polygon points="1097,0 1607,0 1607,98 1170,98" fill="var(--white)"/>
    <text class="brand-name" x="1530" y="66" font-size="50" text-anchor="end">CoverLantern</text>

    <text class="headline" x="1538" y="258" font-size="88" text-anchor="end">TERM LIFE</text>
    <text class="headline" x="1538" y="348" font-size="88" text-anchor="end">INSURANCE</text>

    <g class="feature feature--agent" transform="translate(1230,435) scale(1.44)">
      <circle class="feature-disc" r="27"/>
      <circle class="feature-icon-solid" cx="0" cy="-4" r="7"/>
      <path class="feature-icon-solid" d="M-13 14 Q0 0 13 14 Z"/>
      <path class="feature-icon" stroke-width="2.5" d="M-10 -4 Q-10 -16 0 -16 Q10 -16 10 -4"/>
    </g>
    <g class="feature feature--compare" transform="translate(1366,435) scale(1.44)">
      <circle class="feature-disc" r="27"/>
      <path class="feature-icon" stroke-width="3" d="M-8 -10 V8 M-8 -10 H6 M2 -14 L6 -10 L2 -6 M8 10 V-8 M8 10 H-6 M-2 14 L-6 10 L-2 6"/>
    </g>
    <g class="feature feature--apply" transform="translate(1502,435) scale(1.44)">
      <circle class="feature-disc" r="27"/>
      <rect class="feature-icon-solid" x="-14" y="-13" width="24" height="12" rx="2"/>
      <path class="feature-icon-solid" d="M-6 -4 h6 v10 h8 v8 h-14 z"/>
    </g>
    <text class="feature-label" font-size="24" text-anchor="middle">
      <tspan x="1232" y="502">Agent</tspan><tspan x="1232" y="525">Support</tspan>
      <tspan x="1366" y="502">Compare</tspan><tspan x="1366" y="525">&amp; Save</tspan>
      <tspan x="1504" y="502">Apply</tspan><tspan x="1504" y="525">Online</tspan>
    </text>
  </svg>
</div>

</body>
</html>
```